I need professional letterhead for an attorney. I already have my logo (attached). I currently have a project going to get business cards. I would like the letterhead to be classy. It is very important that this letterhead be in a format that I can import it into Microsoft Word 2013. I plan on importing this into Word so I can type my documents directly onto it and electronically send the finished documents to my clients. Thank you very much.

Industry/Entity Type

Attorney

Requirements
Must have
• Here is my info. Please put it all on there:
• Dwight R. Mallory Attorney At Law
• 48613 Brackwell Crescent
• St. Louis, MO 63047
• Telephone: 314-596-2043
• Fax: 800-627-4915
• Email: Dwight@RivermarkWills.com
• Also, I need the ability to import this final design into Microsoft Word 2013 so that I can type directly onto it. I believe I can do that if you hand it over to me as a JPG and a PDF in addition to the other formats. Then I should be able to import it into Word.

```html
<!DOCTYPE html>
<html lang="en">
<head>
<meta charset="utf-8">
<title>Rivermark Wills LLC – Letterhead</title>
<link rel="stylesheet" href="https://fonts.googleapis.com/css2?family=Open+Sans:wght@400;600;700&display=swap">
<style>
  :root {
    --brand-blue: #2c6fb5;
    --ink: #2b2b2b;
    --ink-soft: #555555;
    --paper: #ffffff;
  }
  * { box-sizing: border-box; margin: 0; padding: 0; }
  html, body { width: 849px; height: 1200px; overflow: hidden; background: var(--paper); }
  body { font-family: "Open Sans", Arial, sans-serif; color: var(--ink); }
  .letterhead { position: relative; width: 849px; height: 1200px; }

  .masthead { position: absolute; top: 28px; left: 34px; right: 30px; height: 84px; display: flex; align-items: center; }
  .brand { display: flex; align-items: center; gap: 14px; width: 505px; }
  .brand-mark { width: 40px; height: 40px; background: var(--brand-blue); flex: none; }
  .brand-name { font-weight: 600; color: var(--brand-blue); font-size: 24px; line-height: 1.2; }
  .divider { width: 2px; height: 74px; background: var(--brand-blue); margin: 0 24px 0 10px; flex: none; }
  .contact { display: flex; gap: 28px; font-size: 11.5px; line-height: 18px; color: var(--ink-soft); }
  .contact .label { color: var(--brand-blue); font-weight: 700; margin-right: 5px; }
  .contact-col { white-space: nowrap; }
  .contact-col .indent { padding-left: 15px; }

  .letter { position: absolute; top: 243px; left: 34px; right: 30px; font-size: 14.2px; line-height: 19.5px; color: var(--ink); }
  .salutation { margin-bottom: 8px; }
  .letter p { text-align: justify; margin-bottom: 19.5px; }

  .signature { position: absolute; top: 858px; right: 34px; text-align: right; font-size: 14.2px; line-height: 20px; }
</style>
</head>
<body>
<div class="letterhead">
  <header class="masthead">
    <div class="brand">
      <span class="brand-mark"></span>
      <div class="brand-name">Rivermark Wills LLC</div>
    </div>
    <div class="divider"></div>
    <div class="contact">
      <div class="contact-col">
        <div><span class="label">t:</span>314-596-2043</div>
        <div><span class="label">f:</span>800-627-4915</div>
        <div><span class="label">e:</span>Dwight@RivermarkWills.com</div>
      </div>
      <div class="contact-col">
        <div><span class="label">a:</span>48613 Brackwell Crescent</div>
        <div class="indent">St. Louis, MO 63047</div>
      </div>
    </div>
  </header>

  <main class="letter">
    <div class="salutation">Dear Jane Doe</div>
    <p>Lorem ipsum dolor sit amet, consectetur adipiscing elit. Nam vestibulum sed libero feugiat interdum. Etiam dapibus molestie lacinia. Donec id commodo erat. Fusce tincidunt tortor in ipsum facilisis, convallis consequat risus viverra. Nam sollicitudin nisi non augue dignissim, molestie dignissim tortor elementum. Mauris urna nisl, sagittis a odio nec, sodales dignissim metus. Nam vestibulum, erat a posuere molestie, nisi tellus accumsan orci, venenatis pellentesque lacus mauris ac turpis. Morbi congue mi sed lacus finibus, ut ultricies risus dapibus. Cras dignissim mauris quis nibh dapibus, quis condimentum odio consequat. Sed pulvinar risus congue tristique dignissim. Maecenas suscipit hendrerit purus, nec porttitor libero commodo eget. Nullam blandit convallis eros, et congue risus vestibulum id. Ut id imperdiet enim.</p>
    <p>Aliquam nec purus neque. Cras efficitur mauris pulvinar posuere dictum. Suspendisse malesuada quam a metus vehicula convallis id vitae tortor. Integer finibus varius erat in auctor. Aliquam erat volutpat. Cras hendrerit ullamcorper est, eget convallis leo finibus vitae. Proin commodo risus urna, at aliquam ante convallis vel. Etiam interdum posuere leo, in volutpat mi sodales et. Suspendisse in lacus justo. Sed porta condimentum ex sit amet tristique.</p>
    <p>Phasellus sed velit lectus. Duis tincidunt id ipsum id ullamcorper. Vivamus porta quam eu metus pharetra convallis. Proin a mauris tortor. Aliquam rhoncus accumsan lectus, bibendum dignissim nisl malesuada in. Phasellus neque lectus, tristique in eleifend ut, rutrum tempor dolor. Aliquam quis lorem non mi sodales dignissim. Fusce accumsan nibh ac sagittis consectetur. Suspendisse lobortis, sapien nec auctor commodo, augue nisl cursus orci, et faucibus ipsum libero ac urna. Aliquam tincidunt venenatis accumsan. Donec condimentum posuere mi, eget cursus nunc malesuada nec. In ut libero scelerisque, posuere eros placerat, hendrerit enim. Cras tempus ante velit, ut dictum tellus euismod facilisis. Maecenas sit amet pellentesque velit.</p>
    <p>Integer sed libero finibus, pharetra dolor sollicitudin, auctor metus. Sed nec est sodales, consequat leo ac, malesuada est. Sed pulvinar erat id congue consectetur. Pellentesque habitant morbi tristique senectus et netus et malesuada fames ac turpis egestas. Fusce luctus tellus vel eros viverra volutpat. Aenean id odio in sem congue elementum. Proin quis ipsum augue. Integer egestas justo et magna aliquam faucibus. Nam pellentesque efficitur egestas.</p>
  </main>

  <footer class="signature">
    <div>Dwight R. Mallory</div>
    <div>Attorney At Law</div>
  </footer>
</div>
</body>
</html>
```